Brindlewick Music Studio needs a promotional postcard design

We are looking for a postcard design for a small business that provides clients with private music lesson instruction. We are looking for a design that will convey the message of "music is fun for kids" that will appeal to parents and encourage them to sign up. We have a company logo that should be used and our color scheme is teal and turquoise. All of our contact info should be displayed as well.

Target Market(s)

Parents with young kids

Contact Information for Business Card

web: www.brindlewickmusicstudio.example
email: lessons@brindlewickmusicstudio.example
phone: 202-555-0147

Font styles to use
Serif
Sans Serif

Colors
33b8a4
86cfc6
0456a4
87cfc6

Requirements
Must have
• Music lessons in your home
• Creating little stars one at a time
• Sign Up Now
• Please use these images:
Nice to have
• Something like this sample postcard:

```html
<!DOCTYPE html>
<html lang="en">
<head>
<meta charset="utf-8">
<title>Brindlewick Music Studio – Postcard</title>
<link rel="stylesheet" href="https://fonts.googleapis.com/css2?family=Lora:wght@400&family=Source+Sans+3:wght@400&family=Libre+Caslon+Text&display=swap">
<style>
  :root {
    --teal: #3fb0b0;
    --ink: #2b2b2b;
    --paper: #fafafa;
    --backdrop: #e6e6e6;
    --stamp: #c6c6c6;
    --rule: #8a8a8a;
    --photo-warm-a: #9a7a58;
    --photo-warm-b: #3b2f2a;
    --photo-stage-a: #0b0b10;
    --photo-stage-b: #2a2824;
    --photo-stage-floor: #d9d2c2;
    --photo-piano-a: #0c1030;
    --photo-piano-b: #1b1f3a;
  }
  * { margin: 0; padding: 0; box-sizing: border-box; }
  html, body { width: 1200px; height: 802px; overflow: hidden; }
  body { background: var(--backdrop); position: relative; }

  .postcard {
    position: absolute;
    top: 274px;
    width: 443px;
    height: 264px;
    background: var(--paper);
    overflow: hidden;
  }
  .postcard--front { left: 136px; }
  .postcard--back { left: 624px; }

  /* Front */
  .brand {
    position: absolute;
    left: 14px;
    top: 40px;
    display: flex;
    align-items: center;
    gap: 10px;
  }
  .brand__dot {
    width: 62px; height: 62px;
    border-radius: 50%;
    background: var(--teal);
    flex: none;
  }
  .brand__name {
    font-family: "Lora", serif;
    font-weight: 400;
    font-size: 21px;
    line-height: 1.1;
    color: var(--teal);
  }
  .tagline {
    position: absolute;
    left: 0; width: 231px;
    top: 113px;
    text-align: center;
    font-family: "Libre Caslon Text", serif;
    font-size: 17px;
    line-height: 25px;
    color: var(--ink);
    letter-spacing: -0.3px;
  }
  .contact {
    position: absolute;
    left: 24px;
    top: 176px;
    list-style: none;
    font-family: "Source Sans 3", sans-serif;
    font-size: 10.3px;
    line-height: 21px;
    color: var(--ink);
    white-space: nowrap;
  }
  .contact__label { color: var(--teal); }

  .photo { position: absolute; }
  .photo--kid {
    left: 231px; top: 0; width: 212px; height: 264px;
    background: linear-gradient(160deg, var(--photo-warm-a), var(--photo-warm-b));
  }

  /* Back */
  .stamp-box {
    position: absolute;
    left: 39px; top: 37px;
    width: 66px; height: 66px;
    background: var(--stamp);
  }
  .address-line {
    position: absolute;
    left: 39px; width: 150px;
    height: 0;
    border-top: 1px solid var(--rule);
  }
  .photo--piano {
    left: 209px; top: 70px; width: 101px; height: 140px;
    border: 3px solid #fff;
    background: linear-gradient(180deg, var(--photo-piano-a), var(--photo-piano-b));
    z-index: 2;
  }
  .photo--violin {
    left: 268px; top: 0; width: 175px; height: 264px;
    background: linear-gradient(180deg, var(--photo-stage-a) 0%, var(--photo-stage-b) 78%, var(--photo-stage-floor) 100%);
  }
</style>
</head>
<body>

<section class="postcard postcard--front">
  <div class="brand">
    <span class="brand__dot"></span>
    <span class="brand__name">Brindlewick<br>Music Studio</span>
  </div>

  <h1 class="tagline">MUSIC IS FUN<br>FOR KIDS</h1>

  <ul class="contact">
    <li><span class="contact__label">P:</span> 202-555-0147</li>
    <li><span class="contact__label">E:</span> lessons@brindlewickmusicstudio.example</li>
    <li><span class="contact__label">W:</span> www.brindlewickmusicstudio.example</li>
  </ul>

  <div class="photo photo--kid" role="img" aria-label="Photo of a smiling young girl making a peace sign at home, violin in the background"></div>
</section>

<section class="postcard postcard--back">
  <div class="stamp-box"></div>
  <div class="address-line" style="top:140px"></div>
  <div class="address-line" style="top:168px"></div>
  <div class="address-line" style="top:196px"></div>
  <div class="address-line" style="top:227px"></div>

  <div class="photo photo--violin" role="img" aria-label="Photo of a young girl in a velvet dress holding a violin on stage"></div>
  <div class="photo photo--piano" role="img" aria-label="Photo of a young girl in a white dress playing a grand piano at a recital"></div>
</section>

</body>
</html>
```